Security doors and flyscreens

We need business cards for our company called K & M Distributors. We quote, manufacture and install security doors and flyscreens.

Industry/Entity Type

Security

Contact Information for Business Card

K & M DISTRIBUTORS
17 Larkvale Rd. Brindlevale 3091
Ph: 8157 2604
Fax: 8157 2609
Gavin: 0419 275 916
Email: gatesupplier@mailbox-example.net

```html
<!DOCTYPE html>
<html lang="en">
<head>
<meta charset="utf-8">
<title>K &amp; M Distributors – Business Card</title>
<link href="https://fonts.googleapis.com/css2?family=Michroma&family=Oswald:wght@700&family=Open+Sans:wght@400;600&display=swap" rel="stylesheet">
<style>
  :root {
    --backdrop-top: #9a9a9a;
    --backdrop-bottom: #f2f2f2;
    --card-white: #ffffff;
    --brand-red: #e0181f;
    --brand-red-dark: #a80f14;
    --ink: #111111;
    --panel-dark: #1c1c1c;
    --panel-darker: #0c0c0c;
    --text-light: #ffffff;
    --divider: #bdbdbd;
  }
  * { box-sizing: border-box; margin: 0; padding: 0; }
  html, body { width: 1200px; height: 900px; overflow: hidden; }
  body {
    background: linear-gradient(180deg, var(--backdrop-top) 0%, var(--backdrop-bottom) 70%);
    position: relative;
    font-family: "Open Sans", sans-serif;
  }
  .business-card {
    position: absolute;
    left: 110px; top: 165px;
    width: 980px; height: 570px;
    border-radius: 40px;
    overflow: hidden;
    background: var(--card-white);
    box-shadow: 0 18px 40px rgba(0,0,0,0.35);
  }
  .brand {
    position: absolute; left: 0; top: 0; width: 100%; height: 300px;
    display: flex; flex-direction: column; align-items: center; justify-content: flex-end;
    padding-bottom: 28px;
  }
  .brand-square {
    width: 150px; height: 150px;
    background: var(--brand-red);
    margin-bottom: 26px;
  }
  .brand-name {
    font-family: "Michroma", sans-serif;
    font-size: 34px; letter-spacing: 1px;
    color: var(--ink);
  }
  .tagline-band {
    position: absolute; left: 0; top: 300px; width: 100%; height: 40px;
    background: var(--brand-red);
    border-top: 3px solid var(--brand-red-dark);
    border-bottom: 3px solid #9b9b9b;
    display: flex; align-items: center; justify-content: center;
  }
  .tagline {
    font-family: "Oswald", sans-serif; font-weight: 700;
    font-size: 19px; letter-spacing: 2.2px;
    color: var(--ink); text-transform: uppercase;
    white-space: nowrap;
  }
  .contact-panel {
    position: absolute; left: 0; top: 340px; width: 100%; height: 230px;
    background: linear-gradient(180deg, var(--panel-dark), var(--panel-darker));
  }
  .person {
    position: absolute; right: 530px; top: 36px; text-align: right;
  }
  .person-name { font-size: 32px; font-weight: 600; color: var(--brand-red); line-height: 1.15; }
  .person-role { font-size: 24px; color: var(--text-light); }
  .divider {
    position: absolute; left: 470px; top: 20px; width: 2px; height: 170px;
    background: var(--divider);
  }
  .contact-list {
    position: absolute; left: 490px; top: 24px; list-style: none;
  }
  .contact-list li {
    display: flex; align-items: center; gap: 8px;
    font-size: 21px; color: var(--text-light); line-height: 32px;
    white-space: nowrap;
  }
  .contact-list svg { width: 24px; height: 24px; fill: var(--brand-red); flex: none; }
</style>
</head>
<body>
  <div class="business-card">
    <header class="brand">
      <div class="brand-square"></div>
      <div class="brand-name">K &amp; M DISTRIBUTORS</div>
    </header>

    <div class="tagline-band">
      <p class="tagline">Specialize in manufacturing &amp; installation of security doors and flyscreens</p>
    </div>

    <section class="contact-panel">
      <div class="person">
        <p class="person-name">Gavin Hartley</p>
        <p class="person-role">manager</p>
      </div>
      <div class="divider"></div>
      <ul class="contact-list">
        <li>
          <svg viewBox="0 0 24 24"><path d="M12 3 1 12h3v9h6v-6h4v6h6v-9h3z"/></svg>
          17 Larkvale Rd. Brindlevale 3091
        </li>
        <li>
          <svg viewBox="0 0 24 24"><path d="M6.6 10.8a15 15 0 0 0 6.6 6.6l2.2-2.2c.3-.3.7-.4 1-.2 1.1.4 2.3.6 3.6.6.6 0 1 .4 1 1V20c0 .6-.4 1-1 1A17 17 0 0 1 3 4c0-.6.4-1 1-1h3.5c.6 0 1 .4 1 1 0 1.3.2 2.5.6 3.6.1.3 0 .7-.2 1z"/></svg>
          8157 2604
        </li>
        <li>
          <svg viewBox="0 0 24 24"><path d="M6 2h9l3 3v5H6zM3 11h18v9H3zm3 3v2h3v-2zm5 0v2h3v-2zm5 0v2h3v-2z"/></svg>
          8157 2609
        </li>
        <li>
          <svg viewBox="0 0 24 24"><path d="M7 1h10a2 2 0 0 1 2 2v18a2 2 0 0 1-2 2H7a2 2 0 0 1-2-2V3a2 2 0 0 1 2-2zm1 3v9h8V4zm0 11v2h2v-2zm3 0v2h2v-2zm3 0v2h2v-2zm-6 3v2h2v-2zm3 0v2h2v-2zm3 0v2h2v-2z"/></svg>
          0419 275 916
        </li>
        <li>
          <svg viewBox="0 0 24 24"><path d="M2 8 12 2l10 6v13H2zm2 2 8 5 8-5-8-5z"/></svg>
          gatesupplier@mailbox-example.net
        </li>
      </ul>
    </section>
  </div>
</body>
</html>
```